Creating business cards for our new private medical clinic in London

Hey everyone,

We are starting a new private medical clinic in central London. We already have our logo (please see the 2 different layouts of the logo attached.) Please note that we are not restricted to using only this font in the card though.

The cards will be printed by "Plinth." The cards have a textured surface and a coloured middle layer - please see this webpage for the exact product spec (https://www.plinthprint.example/uk/products/velour/business-cards.html). We're overall looking for a modern yet highly professional look. We'd like the cards to have Square edges and NOT rounded please.

We need a standard card that uses one or both of our logo's colours (blue and green), and another card for premium customers, that uses black with either gold/silver/bronze. On the black coloured cads, please could you add the word "Onyx Tier" or the word "Onyx" under the logo text - wherever you think it looks best?

_________________

AMENDMENT TO BRIEF:

1) The first batch of our cards are to be promotional cards and need to have more information. Could please have one card that is more like an "information card" that has the following information: - (There's a lot there and we might need to slim this down once we see the cards.)

GP appointments £70
-Feeling unwell
-Referrals to private specialists
-Sexual health check up
-Contraception
-Second opinion

Launch Offer
First appointment £40 with this card until 30 September 2017

Book online

2) Could you see whether we could add a 'strap line' to the card, something like: “Keep Well Daily”

_____________

The files attached have 2 versions of our logo - one linear and with the words 'stacked'; we think that the stacked logo may work better for the business card but we'd love to see different versions.

On one side of the card could we please see a coloured background, with a design containing our logo? On the other side of the card, please could we have a different coloured or white background and the information below.

Address: THE HARROWBY CLINIC @ PeakForm, 19 Pellbrook Lane, London, EC2P 4QX
Open: Mon-Fri (early & late appointments)
Book Online: www.harrowbyclinic.example
Email: bookings@harrowbyclinic.example
Phone number: (We don't have this yet - but please leave a space for this to go into.)

Other possible design features:

Because our clinic is located in the financial district of London, anything that represents this (e.g. The City of London's skyline - i.e. financial district - could look nice (example buildings include: The Thimble, The Lantern, The Wedge, St Orin's Minster, Keep of Brandmoor, Fenwell Bridge, The Spindle). We wondered whether a outline or drawing of these buildings in the background of the card could look nice. Please see the image link below to get an idea of the skyline we're looking for:

https://img.pictovault.example/z/skyline-sketch-pastel-old-and-new-buildings-81920457.jpg

The following image links are examples of cards that we've seen online and like the overall feel of (of course our colours are different):

http://www.cardnook.example/misc/2/nicecards/73019264810.jpg
http://printfox.example/wp-content/uploads/2013/01/sleek-business-cards-sample.jpg
https://cardgallery.example/wp-content/uploads/20417-sleek-business-card-preview.jpg
http://www.tembly.example/wp-content/uploads/edd/2015/08/Clean-Studio-Business-Card-Template-Preview.jpg
http://lorvenpress.example/wp-content/uploads/2017/01/make-a-business-card-sleek-card-ideas-kq82.jpg
http://brightinkhub.example/resources/files/articles/mantel-print/copper-foil-business-cards.jpg

STATIONARY:
We will also need the following stationary designed by our chosen designer. We’d like stationary to use one or both the colours of our logo (ie Green and Blue). Please use these colours to add any additional design features to stationary - other similar palette colours can also be used. Our logo font is - abeatbyKai - and this could be used in other parts of the stationary, but please feel free to try other fonts too. We prefer sans serif fonts.

Overall - we are open to all ideas but we need a look and feel that looks modern and highly professional. For our letter, prescription and medical report templates we need these to be PDFs and word processing files that can merge relevant data and text into different sections.

The information required on various pieces of stationary are as follows:

Letterheads:
These need to have:
Clinic's: Logo / Address / Phone Number / Website / Email address / Recipients address.
The letter can have address data either at the top or as a footer. We're happy to see designs that use either to see which one looks best (same goes for other pieces of stationary too.)

Invoices:
Invoice number: (Unique code for document)
Invoice Date:
Clinic’s: Logo / Address / Phone Number / Website / Email address
Services: Service Code / Name of Service / Price
Total Price:
PAYRO, Coinvault and Northern Tender Logos
Patient details: Patient’s Name / Address

Prescription Pads:
Prescription number: (Unique code for document)
Clinic details: Clinic’s Logo / Address / Phone Number / Website / Email address
Patient details needed include: Patient’s Name / Date of birth / address
Blank space required to write the name of medication
Doctors Signature: and space for signature
MRB Number: and space for this to be entered

Templates for our medical reports:
These are reports we will be printed (on good quality paper) for patients after they have had a complete health check. They will include a text summary, and the results of any tests (with graphs) and images of scans. Please could we see how text/titles/headings/tables etc could be styled?
They will need the following details: -
Clinic details needed include: Clinic’s Logo / Address / Phone Number / Website / Email address
Date of Report:
Then the following sections need to be includes:
1) Free Text Space
2) Space for images and text
3) Space for blood test and text

___________________

Thanks so much everyone.

All the best,

Tev and Dale

Target Market(s)

City of London
Private Healthcare

Industry/Entity Type

Health Care

Contact Information for Business Card

Font styles to use
Sans Serif

Colors
33a6d7
25a0d3
add136
9bcb3c
cadf82
85acd3
3276b5
0255a3
85cae6

Requirements
Must have
• Please see project description for details.
Nice to have
• Perhaps a outline/drawing/illustration of the City of London skyline (i.e. the Thimble and surrounding buildings)

```html
<!DOCTYPE html>
<html lang="en">
<head>
<meta charset="utf-8">
<title>The Harrowby Clinic – Business Cards</title>
<link href="https://fonts.googleapis.com/css2?family=Quicksand:wght@400&family=Open+Sans:wght@400;600&display=swap" rel="stylesheet">
<style>
  :root {
    --page: #ecebe8;
    --onyx: #121212;
    --paper: #ffffff;
    --clinic-blue: #33a6d7;
    --clinic-green: #add136;
    --muted: #8a8a8a;
    --on-green: #ffffff;
  }
  html, body {
    margin: 0;
    width: 1200px;
    height: 1200px;
    overflow: hidden;
    background: var(--page);
  }
  .sheet {
    position: relative;
    width: 1200px;
    height: 1200px;
  }
  .card {
    position: absolute;
    left: 160px;
    width: 880px;
    height: 500px;
    overflow: hidden;
    box-shadow: 0 10px 28px rgba(0,0,0,.18);
  }
  .card--front { top: 60px; background: var(--onyx); }
  .card--back  { top: 640px; background: var(--paper); }

  .brand {
    position: absolute;
    display: flex;
    align-items: center;
    gap: 18px;
  }
  .brand__mark {
    width: 22px; height: 22px;
    background: var(--clinic-blue);
  }
  .brand__text { border-left: 2px solid var(--clinic-blue); padding-left: 16px; }
  .brand__name {
    font-family: "Quicksand", sans-serif;
    font-weight: 400;
    color: var(--clinic-blue);
    line-height: 1;
    margin: 0;
  }
  .brand__tag {
    font-family: "Open Sans", sans-serif;
    font-weight: 400;
    color: var(--muted);
    letter-spacing: .12em;
    margin: 8px 0 0;
  }
  .card--front .brand { left: 300px; top: 190px; }
  .card--front .brand__name { font-size: 52px; }
  .card--front .brand__tag { font-size: 12px; }
  .card--front .brand__text { padding-top: 6px; padding-bottom: 6px; }

  .card--back .brand { left: 60px; top: 226px; }
  .card--back .brand__name { font-size: 38px; }
  .card--back .brand__tag { font-size: 10px; text-align: right; }

  .panel-shape { position: absolute; inset: 0; }

  .contact {
    position: absolute;
    left: 560px;
    top: 86px;
    width: 300px;
    color: var(--on-green);
    font-family: "Open Sans", sans-serif;
  }
  .contact__title {
    font-family: "Quicksand", sans-serif;
    font-weight: 400;
    font-size: 25px;
    letter-spacing: .04em;
    margin: 0 0 18px;
    padding-bottom: 6px;
    border-bottom: 1.5px solid var(--on-green);
  }
  .contact__list { list-style: none; margin: 0; padding: 0; }
  .contact__item {
    display: flex;
    gap: 12px;
    font-size: 14px;
    line-height: 1.45;
    margin-bottom: 9px;
  }
  .contact__icon { flex: 0 0 16px; width: 16px; height: 16px; margin-top: 2px; }
</style>
</head>
<body>
<main class="sheet">

  <section class="card card--front" aria-label="Card front">
    <div class="brand">
      <span class="brand__mark"></span>
      <div class="brand__text">
        <p class="brand__name">The Harrowby<br>Clinic</p>
        <p class="brand__tag">PRIVATE GENERAL PRACTICE</p>
      </div>
    </div>
  </section>

  <section class="card card--back" aria-label="Card back">
    <svg class="panel-shape" width="880" height="500" viewBox="0 0 880 500" aria-hidden="true">
      <polygon points="510,0 880,0 880,500 540,500 540,420 520,400 520,250 500,230 500,20" fill="var(--clinic-green)"/>
      <polyline points="484,0 484,60" stroke="var(--clinic-blue)" stroke-width="4" fill="none"/>
      <polyline points="486,250 486,330 506,350" stroke="var(--clinic-blue)" stroke-width="4" fill="none"/>
      <polyline points="520,420 540,440 540,500" stroke="var(--clinic-green)" stroke-width="4" fill="none"/>
    </svg>

    <div class="brand">
      <span class="brand__mark"></span>
      <div class="brand__text">
        <p class="brand__name">The Harrowby Clinic</p>
        <p class="brand__tag">PRIVATE GENERAL PRACTICE</p>
      </div>
    </div>

    <div class="contact">
      <h2 class="contact__title">THE HARROWBY CLINIC</h2>
      <ul class="contact__list">
        <li class="contact__item">
          <svg class="contact__icon" viewBox="0 0 16 16"><path d="M8 1a5 5 0 0 0-5 5c0 4 5 9 5 9s5-5 5-9a5 5 0 0 0-5-5zm0 7a2 2 0 1 1 0-4 2 2 0 0 1 0 4z" fill="currentColor"/></svg>
          <span>PeakForm, 19 Pellbrook Lane<br>London, EC2P 4QX</span>
        </li>
        <li class="contact__item">
          <svg class="contact__icon" viewBox="0 0 16 16"><path d="M4 1l3 3-2 2c1 2 3 4 5 5l2-2 3 3-2 3C7 15 1 9 1 3z" fill="currentColor"/></svg>
          <span>+00 - 000 - 0000</span>
        </li>
        <li class="contact__item">
          <svg class="contact__icon" viewBox="0 0 16 16"><circle cx="8" cy="8" r="6.5" fill="none" stroke="currentColor" stroke-width="1.5"/><path d="M8 4v4l3 2" fill="none" stroke="currentColor" stroke-width="1.5"/></svg>
          <span>Mon-Fri (early &amp; late appointments)</span>
        </li>
        <li class="contact__item">
          <svg class="contact__icon" viewBox="0 0 16 16"><circle cx="8" cy="8" r="6.5" fill="none" stroke="currentColor" stroke-width="1.5"/><path d="M1.5 8h13M8 1.5c3 3 3 10 0 13M8 1.5c-3 3-3 10 0 13" fill="none" stroke="currentColor" stroke-width="1.2"/></svg>
          <span>www.harrowbyclinic.example</span>
        </li>
        <li class="contact__item">
          <svg class="contact__icon" viewBox="0 0 16 16"><rect x="1.5" y="3.5" width="13" height="9" fill="none" stroke="currentColor" stroke-width="1.5"/><path d="M1.5 3.5l6.5 5 6.5-5" fill="none" stroke="currentColor" stroke-width="1.5"/></svg>
          <span>bookings@harrowbyclinic.example</span>
        </li>
      </ul>
    </div>
  </section>

</main>
</body>
</html>
```